Homeopathic medicinal cream label design

I am looking for a product label design for a medicinal (cannabis) topical cream to be sold to medical marijuana patients. It is a new product that has not yet established a brand identity. It will be sold in 2 and 4 ounce containers so the design needs to work on a small scale. The design may be used for other branding as well.

Target Market(s)

Medical marijuana users in states where it is legal. The product should appeal to both men and women to promote pain relief in muscles and joints. It can also be used as a massage cream for general relaxation.

Industry/Entity Type

Medical

Font styles to use
Sans Serif

Requirements
Must have
• Something that reflects the company name - The Quiet Lark - and the name of the initial product - Meadow Balm Blend.
• In addition to the name of the company and the name of the product, other information to include would be the volume being sold (e.g. 4 oz.), that it is a topical botanical ointment, and its ingredients (coconut oil, beeswax, soy lecithin, and eight all natural botanical oils - cannabis, lavender, eucalyptus, peppermint, rosemary, cinnamon, clove, and lemon). The label should clearly state that the product is for topical use only.
• The information must fit on the space available on the package. The 4 oz. container's lid has approximately 2 1/8" of surface area. The width of the label on the lid should be approximately 1 7/8". On the container's body, the height of the surface area is approximately 1", and the width is approximately 8 1/2 inches. The width of the label should be around 8 inches to allow room for it to be applied to the container. I have posted a photo of the 4 oz. container and the 2 oz. container. I have also posted a photo of the labeling of some of our competitors with similar products.
Nice to have
• We are thinking of having the logo on the lid of the container, and a circle bordering the lid that may have text in it. (See the "Amber Owl" label attached as an exemplar).
• The label on the body of the container (or maybe on the bottom on the container) would list other information about the product, such as its ingredients and our contact information.

```html
<!DOCTYPE html>
<html lang="en">
<head>
<meta charset="utf-8">
<title>The Quiet Lark – Meadow Balm Blend Labels</title>
<link rel="stylesheet" href="https://fonts.googleapis.com/css2?family=Oswald:wght@500;600&family=Roboto+Condensed:wght@400;700&display=swap">
<style>
  :root {
    --bg-top: #eeeeee;
    --bg-bottom: #ffffff;
    --green-dark: #1c8a3a;
    --green-mid: #3faa2e;
    --lime: #c6dc38;
    --lime-light: #dfe94a;
    --lime-deep: #9ec22a;
    --ink: #111111;
    --brown-ink: #2a1010;
    --grey-band: #a9a9a9;
    --dim-line: #222222;
    --white: #ffffff;
  }
  * { box-sizing: border-box; margin: 0; padding: 0; }
  html, body { width: 1200px; height: 1000px; overflow: hidden; }
  body {
    position: relative;
    background: linear-gradient(180deg, var(--bg-top) 0%, var(--bg-bottom) 45%);
    font-family: "Roboto Condensed", sans-serif;
    color: var(--ink);
  }

  /* Brand name block */
  .brand-mark {
    position: absolute; left: 170px; top: 150px; width: 360px;
    display: flex; align-items: center; gap: 18px;
  }
  .brand-mark__dot { width: 44px; height: 44px; border-radius: 50%; background: var(--green-mid); flex: none; }
  .brand-mark__name { font-family: "Roboto Condensed", sans-serif; font-weight: 400; font-size: 58px; color: var(--brown-ink); white-space: nowrap; }

  /* Dimension annotations */
  .dim { position: absolute; }
  .dim__label { position: absolute; font-family: "Roboto Condensed", sans-serif; font-weight: 700; font-size: 24px; color: var(--ink); white-space: nowrap; }
  .dim__label small { font-size: 17px; }

  /* Lid label */
  .lid-label { position: absolute; left: 234px; top: 382px; width: 248px; height: 248px; }

  /* Body label */
  .body-label {
    position: absolute; left: 95px; top: 720px; width: 1060px; height: 133px;
    background: var(--lime);
    border-top: 8px solid var(--grey-band);
    border-bottom: 8px solid var(--grey-band);
    overflow: hidden;
  }
  .body-label__about {
    position: absolute; left: 28px; top: 10px; width: 240px; text-align: center;
    font-size: 10px; line-height: 1.35;
  }
  .body-label__about-title {
    display: inline-block; font-weight: 700; font-size: 11px; color: var(--green-dark);
    text-decoration: underline; margin-bottom: 4px;
  }
  .body-label__about-note { font-weight: 700; margin-top: 1px; }
  .body-label__brand-box {
    position: absolute; left: 263px; top: -8px; width: 142px; height: 133px;
    background: var(--green-dark); border: 2px solid var(--lime-light);
    display: flex; flex-direction: column; align-items: center; justify-content: center; gap: 10px;
  }
  .body-label__brand-dot { width: 34px; height: 34px; border-radius: 50%; background: var(--white); }
  .body-label__brand-name { font-size: 19px; color: var(--white); white-space: nowrap; }
  .body-label__title {
    position: absolute; left: 415px; top: 22px;
    font-family: "Oswald", sans-serif; font-weight: 600; font-size: 30px; line-height: 1;
    color: var(--ink); padding-bottom: 5px; border-bottom: 3px solid #7a7a7a; white-space: nowrap;
  }
  .body-label__subtitle {
    position: absolute; left: 415px; top: 69px;
    font-family: "Oswald", sans-serif; font-weight: 500; font-size: 13px; letter-spacing: .5px; color: var(--green-dark);
  }
  .body-label__volume { position: absolute; left: 415px; top: 89px; font-size: 12px; }
  .body-label__art {
    position: absolute; left: 690px; top: 0; width: 200px; height: 117px;
    background: radial-gradient(ellipse at center, #5f9e3a 0%, rgba(120,170,50,.55) 55%, rgba(198,220,56,0) 100%);
  }
  .body-label__info {
    position: absolute; left: 821px; top: 6px; width: 230px;
    font-size: 9px; line-height: 1.22;
  }
  .body-label__info-heading { font-weight: 700; color: var(--green-dark); font-size: 9.5px; }
  .body-label__contact { margin-top: 4px; }
  .body-label__contact strong { display: block; }
  .body-label__web { font-weight: 700; }
  .body-label__mini-brand {
    position: absolute; right: 12px; bottom: 8px; font-size: 10px; color: var(--ink);
    display: flex; align-items: center; gap: 4px;
  }
  .body-label__mini-dot { width: 10px; height: 10px; border-radius: 50%; background: var(--white); }
</style>
</head>
<body>

  <div class="brand-mark">
    <span class="brand-mark__dot"></span>
    <span class="brand-mark__name">the quiet lark</span>
  </div>

  <svg class="dim" style="left:195px;top:330px" width="300" height="310" viewBox="0 0 300 310">
    <g stroke="var(--dim-line)" fill="none" stroke-width="1">
      <line x1="39" y1="10" x2="39" y2="30"/>
      <line x1="287" y1="10" x2="287" y2="30"/>
      <line x1="39" y1="30" x2="287" y2="30"/>
      <line x1="0" y1="52" x2="90" y2="52"/>
      <line x1="0" y1="300" x2="110" y2="300" stroke-dasharray="4 3"/>
      <line x1="8" y1="52" x2="8" y2="300"/>
      <line x1="39" y1="30" x2="39" y2="120" stroke-dasharray="4 3"/>
      <line x1="287" y1="30" x2="287" y2="120" stroke-dasharray="4 3"/>
    </g>
    <g fill="var(--dim-line)">
      <path d="M39 30 l8 -4 v8 z"/><path d="M287 30 l-8 -4 v8 z"/>
      <path d="M8 52 l-4 8 h8 z"/><path d="M8 300 l-4 -8 h8 z"/>
    </g>
  </svg>
  <div class="dim__label" style="left:327px;top:324px">1 <small>7/8”</small></div>
  <div class="dim__label" style="left:165px;top:495px;transform:rotate(-90deg)">1 <small>7/8”</small></div>

  <svg class="lid-label" viewBox="0 0 248 248" role="group" aria-label="Lid label">
    <defs>
      <clipPath id="lid-clip"><circle cx="124" cy="124" r="118"/></clipPath>
      <radialGradient id="lid-sky" cx="50%" cy="35%" r="70%">
        <stop offset="0" stop-color="#eef25a"/>
        <stop offset=".55" stop-color="#b9d830"/>
        <stop offset="1" stop-color="#3faa2e"/>
      </radialGradient>
      <radialGradient id="lid-art" cx="45%" cy="50%" r="60%">
        <stop offset="0" stop-color="#5a9a3a"/>
        <stop offset="1" stop-color="#c6dc38" stop-opacity="0"/>
      </radialGradient>
    </defs>
    <circle cx="124" cy="124" r="124" fill="var(--green-dark)"/>
    <g clip-path="url(#lid-clip)">
      <rect x="0" y="0" width="248" height="104" fill="url(#lid-sky)"/>
      <rect x="0" y="140" width="248" height="108" fill="var(--lime)"/>
      <rect x="0" y="102" width="248" height="40" fill="var(--white)"/>
      <line x1="0" y1="106" x2="248" y2="106" stroke="var(--lime-deep)" stroke-width="1.5"/>
      <line x1="0" y1="138" x2="248" y2="138" stroke="var(--lime-deep)" stroke-width="1.5"/>
      <rect x="20" y="142" width="130" height="100" fill="url(#lid-art)" role="img" aria-label="Botanical sketch of rosemary, cinnamon sticks, star anise, lemon slice and cannabis leaf"/>
      <line x1="138" y1="152" x2="138" y2="222" stroke="var(--green-dark)" stroke-width="1"/>
    </g>
    <circle cx="124" cy="42" r="10" fill="var(--white)"/>
    <text x="124" y="91" text-anchor="middle" font-family="Roboto Condensed, sans-serif" font-size="17" fill="var(--brown-ink)">the quiet lark</text>
    <text x="124" y="131" text-anchor="middle" font-family="Oswald, sans-serif" font-weight="600" font-size="23" fill="var(--ink)">•MEADOW BALM BLEND•</text>
    <g font-family="Oswald, sans-serif" font-weight="500" font-size="14" fill="var(--green-dark)">
      <text x="144" y="167">Natural</text>
      <text x="144" y="184">Botanical</text>
      <text x="144" y="201">Ointment</text>
    </g>
    <text x="144" y="218" font-family="Roboto Condensed, sans-serif" font-size="11" fill="var(--ink)">4 oz.</text>
  </svg>

  <svg class="dim" style="left:55px;top:670px" width="1110" height="195" viewBox="0 0 1110 195">
    <g stroke="var(--dim-line)" fill="none" stroke-width="1">
      <line x1="40" y1="10" x2="40" y2="40"/>
      <line x1="1100" y1="10" x2="1100" y2="40"/>
      <line x1="40" y1="22" x2="1100" y2="22"/>
      <line x1="10" y1="50" x2="40" y2="50"/>
      <line x1="10" y1="183" x2="40" y2="183"/>
      <line x1="13" y1="50" x2="13" y2="183"/>
    </g>
    <g fill="var(--dim-line)">
      <path d="M40 22 l8 -4 v8 z"/><path d="M1100 22 l-8 -4 v8 z"/>
      <path d="M13 50 l-4 8 h8 z"/><path d="M13 183 l-4 -8 h8 z"/>
    </g>
  </svg>
  <div class="dim__label" style="left:610px;top:660px">8”</div>
  <div class="dim__label" style="left:38px;top:770px;transform:rotate(-90deg)">1”</div>

  <section class="body-label" aria-label="Body label">
    <div class="body-label__about">
      <span class="body-label__about-title">MEADOW BALM BLEND</span>
      <p>Is a uniquely formulated aromatic blend of hand-selected botanical and essential oils designed to provide relief for tired muscles and joints. This ointment contains no chemicals, artificial ingredients, fillers, or toxins.</p>
      <p class="body-label__about-note">FOR TOPICAL USE ONLY</p>
    </div>

    <div class="body-label__brand-box">
      <span class="body-label__brand-dot"></span>
      <span class="body-label__brand-name">the quiet lark</span>
    </div>

    <h1 class="body-label__title">MEADOW BALM BLEND</h1>
    <p class="body-label__subtitle">NATURAL BOTANICAL OINTMENT</p>
    <p class="body-label__volume">4 oz.</p>

    <div class="body-label__art" role="img" aria-label="Botanical sketch of rosemary sprigs, lemon slice, cannabis leaf, cinnamon sticks and star anise"></div>

    <div class="body-label__info">
      <p class="body-label__info-heading">INGREDIENTS:</p>
      <p>Coconut oil, beeswax, olive oil, castor oil, cannabis extract, the essential oils of lavender, peppermint, eucalyptus, rosemary, lemon, lemongrass, spearmint, tea tree, cinnamon, camphor, clove, and chamomile. Soy lecithin as an emulsifier.</p>
      <p class="body-label__contact"><strong class="body-label__info-heading">CONTACT US:</strong>hello@quietlarkbalms.com<br><span class="body-label__web">www.quietlarkbalms.com</span></p>
    </div>
    <div class="body-label__mini-brand"><span class="body-label__mini-dot"></span>the quiet lark</div>
  </section>

</body>
</html>
```